Brindle Works Business Card

We need a business card design for an existing company (www.brindle-works.example). The business cards will be by Pavo in their Velta range (http://uk.pavoprint.example/products/velta/business-cards.html).

The card should be landscape, with the full company logo on the reverse side. I would like to have the card to portray a professional image (this is a high technology niche consultancy company). The card should be mostly white but aligned with our website (this is mostly dark colours). I can supply the logo files etc.

Details on the card should include the following:

Name (example: Martin Oakbury)
Position (example: Principal Consultant)
Email Address (example: martin@brindle-works.example)
Mobile Phone Number (example: +44 (0) 7912 604 385)
Website (example: www.brindle-works.example)
Twitter (example: @brindleworksco)
Facebook (example: www.socialhub.example/brindleworksco)

I would like the text on the front of the card to be black. Thanks.

Industry/Entity Type

Business

Requirements
Should not have
• The company address on the card.

```html
<!DOCTYPE html>
<html lang="en">
<head>
<meta charset="utf-8">
<title>Brindle Works Solutions – Business Card</title>
<link rel="stylesheet" href="https://fonts.googleapis.com/css2?family=Questrial&display=swap">
<style>
  :root {
    --stage: #e9e9e9;
    --card-white: #ffffff;
    --card-dark: #2b2d30;
    --brand-orange: #f07a1e;
    --ink: #141414;
    --ink-soft: #3a3a3a;
    --tagline-dark: #e6e6e6;
    --rule-dark: #1f2123;
    --rule-light: #d9d9d9;
    --rule-grey: #8a8a8a;
  }
  * { box-sizing: border-box; margin: 0; padding: 0; }
  html, body { width: 1200px; height: 900px; overflow: hidden; }
  body {
    background: var(--stage);
    font-family: "Questrial", "Century Gothic", sans-serif;
    position: relative;
  }
  .card {
    position: absolute;
    top: 290px;
    width: 530px;
    height: 310px;
    border-radius: 26px;
    overflow: hidden;
    box-shadow: 0 10px 24px rgba(0,0,0,0.18);
  }
  .card--front { left: 55px; background: var(--card-white); }
  .card--back  { left: 615px; background: var(--card-dark); }

  .brand { display: flex; align-items: center; gap: 16px; }
  .brand__dot {
    width: 62px; height: 62px; border-radius: 50%;
    background: var(--brand-orange); flex: none;
  }
  .brand__name {
    color: var(--brand-orange);
    text-transform: uppercase;
    letter-spacing: 1px;
    line-height: 1;
    white-space: nowrap;
  }
  .brand__tagline { letter-spacing: 0.6px; margin-top: 6px; white-space: nowrap; }

  .card--front .brand { position: absolute; left: 26px; top: 58px; }
  .card--front .brand__name { font-size: 27px; }
  .card--front .brand__tagline { font-size: 17px; color: var(--ink-soft); }

  .front__band {
    position: absolute; left: 0; right: 0; top: 152px;
    height: 8px; background: var(--rule-dark);
  }
  .front__band::before {
    content: ""; position: absolute; left: 0; right: 0; top: -4px;
    height: 3px; background: var(--rule-light);
  }

  .person {
    position: absolute; right: 358px; top: 202px; text-align: right;
  }
  .person__name { color: var(--brand-orange); font-size: 16px; }
  .person__role { color: var(--ink); font-size: 13px; margin-top: 5px; }

  .front__divider {
    position: absolute; left: 186px; top: 182px;
    width: 1px; height: 106px; background: var(--rule-grey);
  }

  .contacts {
    position: absolute; left: 198px; top: 188px; list-style: none;
  }
  .contacts li {
    display: flex; align-items: center; gap: 8px;
    font-size: 15px; color: var(--ink); height: 21px; white-space: nowrap;
  }
  .contacts svg { width: 13px; height: 13px; flex: none; }
  .icon-square { width: 12px; height: 12px; background: var(--brand-orange); border-radius: 2px; flex: none; }

  .card--back .brand {
    position: absolute; left: 0; right: 0; top: 60px;
    flex-direction: column; gap: 26px; text-align: center;
  }
  .card--back .brand__dot { width: 120px; height: 120px; }
  .card--back .brand__name { font-size: 30px; }
  .card--back .brand__tagline { font-size: 18px; color: var(--tagline-dark); }
</style>
</head>
<body>

<section class="card card--front" aria-label="Business card front">
  <div class="brand">
    <span class="brand__dot"></span>
    <div>
      <div class="brand__name">Brindle Works Solutions</div>
      <div class="brand__tagline">Smart Systems - Sound Advice - Results</div>
    </div>
  </div>

  <div class="front__band"></div>

  <div class="person">
    <div class="person__name">Martin Oakbury</div>
    <div class="person__role">Principal Consultant</div>
  </div>

  <div class="front__divider"></div>

  <ul class="contacts">
    <li>
      <svg viewBox="0 0 14 14" aria-hidden="true"><rect x="3" y="0.5" width="8" height="13" rx="1.5" fill="none" stroke="var(--brand-orange)" stroke-width="1.6"/><rect x="5" y="2.5" width="4" height="5" fill="var(--brand-orange)"/></svg>
      +44 (0) 7912 604 385
    </li>
    <li>
      <svg viewBox="0 0 14 14" aria-hidden="true"><circle cx="7" cy="7" r="6" fill="none" stroke="var(--brand-orange)" stroke-width="1.4"/><ellipse cx="7" cy="7" rx="2.6" ry="6" fill="none" stroke="var(--brand-orange)" stroke-width="1.2"/><line x1="1" y1="7" x2="13" y2="7" stroke="var(--brand-orange)" stroke-width="1.2"/></svg>
      www.brindle-works.example
    </li>
    <li>
      <svg viewBox="0 0 14 14" aria-hidden="true"><rect x="0.8" y="3" width="12.4" height="9" fill="var(--brand-orange)"/><polyline points="0.8,3 7,8 13.2,3" fill="none" stroke="#fff" stroke-width="1.2"/></svg>
      martin@brindle-works.example
    </li>
    <li><span class="icon-square"></span>@brindleworksco</li>
    <li><span class="icon-square"></span>www.socialhub.example/brindleworksco</li>
  </ul>
</section>

<section class="card card--back" aria-label="Business card back">
  <div class="brand">
    <span class="brand__dot"></span>
    <div>
      <div class="brand__name">Brindle Works Solutions</div>
      <div class="brand__tagline">Smart Systems - Sound Advice - Results</div>
    </div>
  </div>
</section>

</body>
</html>
```